TONVALE - A modern gin bottle label

Design of a bottle label in a modern fresh design. The name of the gin is "TONVALE Phantom Batch K7". Please take a look at the tonvale.de website. on the main page of tonvale.de you can breathe the design direction here: 1) the taste of the gin should be composed of 10 botanicals ... an important scent note. ) a distinctive flavor is spicy and fresh 3.) The filling volume is 0.5 liters 4.) the alcohol content is 43% vol. 5.) the variety is called "dry gin" 6.) tonvale stands for "energy" and "love"

Target Market(s)

Alcohol consumer

Colors

Designer to choose colors to be used in the design.

Requirements
Must have
• the tonvale corporate logo must be included, the name of the gin is "TONVALE Phantom Batch K7"
Nice to have
• Please use the bottles template in the appendix. (The Black Bottles) they can use the saying "DESTILLED & BOTTLED BY OLD MARINER" in small letters

```html
<!DOCTYPE html>
<html lang="en">
<head>
<meta charset="utf-8">
<title>TONVALE Phantom Batch K7 – Dry Gin Label</title>
<link rel="stylesheet" href="https://fonts.googleapis.com/css2?family=Josefin+Sans:wght@600;700&family=Oswald:wght@300;400;500&family=Montserrat:wght@400;600&display=swap">
<style>
  :root {
    --backdrop: #f4f4f2;
    --label-black: #141414;
    --accent-orange: #e8641f;
    --text-white: #f2f2f2;
    --gold-light: #e6d28a;
    --gold-mid: #c2a450;
    --gold-dark: #8c6f2a;
  }
  * { margin: 0; padding: 0; box-sizing: border-box; }
  html, body {
    width: 1200px; height: 2204px; overflow: hidden;
    background: var(--backdrop);
  }
  .canvas { position: relative; width: 1200px; height: 2204px; }

  .label {
    position: absolute; left: 80px; top: 120px;
    width: 1040px; height: 1964px;
    background: var(--label-black);
    border-radius: 28px;
  }

  .brand-vertical {
    position: absolute; left: 70px; top: 420px;
    width: 150px; height: 1300px;
    display: flex; flex-direction: column; justify-content: space-between; align-items: center;
    font-family: "Josefin Sans", sans-serif; font-weight: 700;
    font-size: 118px; line-height: 1; color: var(--accent-orange);
  }
  .brand-rule {
    position: absolute; left: 262px; top: 410px;
    width: 5px; height: 1320px; background: var(--accent-orange);
  }

  .content {
    position: absolute; left: 300px; right: 0; top: 0; bottom: 0;
  }
  .centered { position: absolute; left: 0; right: 0; text-align: center; white-space: nowrap; }

  .logo {
    top: 560px; display: flex; justify-content: center; align-items: center; gap: 18px;
    font-family: "Montserrat", sans-serif; font-weight: 600;
    font-size: 50px; letter-spacing: 7px; color: var(--text-white);
  }
  .logo-mark { width: 34px; height: 34px; background: var(--accent-orange); }

  .edition {
    top: 910px;
    font-family: "Oswald", sans-serif; font-weight: 300;
    font-size: 78px; line-height: 1; letter-spacing: -1px; color: var(--text-white);
  }

  .variety {
    top: 1100px;
    font-family: "Oswald", sans-serif; font-weight: 500;
    font-size: 190px; line-height: 1;
    background: linear-gradient(90deg, var(--gold-dark), var(--gold-light) 35%, var(--gold-mid) 60%, var(--gold-light) 85%, var(--gold-dark));
    -webkit-background-clip: text; background-clip: text; color: transparent;
  }

  .maker {
    top: 1340px;
    font-family: "Oswald", sans-serif; font-weight: 400;
    font-size: 38px; line-height: 1.2; letter-spacing: 1px; color: var(--text-white);
  }

  .divider {
    position: absolute; left: 112px; width: 516px; top: 1480px;
    height: 3px; background: var(--text-white);
  }

  .values {
    position: absolute; left: 112px; width: 516px; top: 1510px; height: 34px;
    border-radius: 17px;
    background: linear-gradient(90deg, var(--gold-dark), var(--label-black) 45%, var(--gold-mid) 70%, var(--gold-light));
    display: flex; justify-content: space-between; align-items: center; padding: 0 28px;
    font-family: "Montserrat", sans-serif; font-weight: 400;
    font-size: 22px; letter-spacing: 5px; color: var(--label-black);
  }
  .values .value-energy { color: var(--gold-light); }

  .volume, .abv {
    position: absolute; top: 1760px;
    font-family: "Montserrat", sans-serif; font-weight: 400;
    font-size: 38px; color: var(--text-white);
  }
  .volume { left: 60px; }
  .abv { right: 90px; }
</style>
</head>
<body>
<div class="canvas">
  <div class="label">
    <div class="brand-vertical" aria-label="TONVALE">
      <span>T</span><span>O</span><span>N</span><span>V</span><span>A</span><span>L</span><span>E</span>
    </div>
    <div class="brand-rule"></div>

    <div class="content">
      <div class="centered logo"><span class="logo-mark"></span><span>TONVALE</span></div>
      <div class="centered edition">PHANTOM BATCH K7</div>
      <div class="centered variety">DRY GIN</div>
      <div class="centered maker">DESTILLED &amp; BOTTLED<br>BY OLD MARINER</div>
      <div class="divider"></div>
      <div class="values"><span class="value-energy">ENERGY</span><span>LOVE</span></div>
      <div class="volume">0,5 l</div>
      <div class="abv">43% vol.</div>
    </div>
  </div>
</div>
</body>
</html>
```